Bref créative
Business Cards and Stationery Project
Verdant Pathways Health and Fitness Center
I need double sided standard sized Business Card [3.5" x 2"]
Use same fonts as used on my logo but also try different fonts
Professional
Marcus T. Delaney
Owner/Health Practitioner
4172 Larchmont Ave S
Lakeford, MN 55788
marcus.delaney@vpwellbody.com
www.vpwellbody.com
Looking for a clean looking business card/stationery. It would be nice to have health center tagline w/ company name one one side. Tagline Where Balanced Living is Your Truest Reward. If possible can there be date and time space for appointment.

```html
<!DOCTYPE html>
<html lang="en">
<head>
<meta charset="utf-8">
<title>Verdant Pathways Health and Fitness Center – Business Cards</title>
<link href="https://fonts.googleapis.com/css2?family=Arimo:ital,wght@0,400;0,700;1,400;1,700&display=swap" rel="stylesheet">
<style>
  :root {
    --sheet: #e6e7e8;
    --card-white: #ffffff;
    --brand-green: #3f9a3a;
    --brand-blue: #1f3e8c;
    --navy-dark: #1a2f78;
    --navy-light: #4a64b4;
    --green-dark: #2f7f2c;
    --green-light: #93c98a;
    --ink: #1b1b1b;
    --rule: #2a2a2a;
  }
  * { margin: 0; padding: 0; box-sizing: border-box; }
  html, body { width: 1200px; height: 698px; overflow: hidden; background: var(--sheet); }
  body { font-family: "Arimo", Arial, sans-serif; color: var(--ink); position: relative; }

  .card {
    position: absolute; width: 560px; height: 323px;
    border: 1px solid #9a9a9a; overflow: hidden;
  }
  .card--front { left: 30px; top: 20px; background: var(--card-white); }
  .card--navy { left: 612px; top: 20px; background: linear-gradient(160deg, var(--navy-light) 0%, var(--brand-blue) 55%, var(--navy-dark) 100%); }
  .card--plain { left: 30px; top: 358px; background: var(--card-white); }
  .card--green { left: 612px; top: 358px; background: linear-gradient(170deg, var(--green-light) 0%, #5fae57 50%, var(--green-dark) 100%); }

  .lockup { position: absolute; display: flex; align-items: center; gap: 8px; white-space: nowrap; }
  .lockup__dot { width: 14px; height: 14px; border-radius: 50%; background: var(--brand-green); flex: none; }
  .lockup__text { display: flex; flex-direction: column; }
  .lockup__name { font-weight: 700; font-size: 22px; color: var(--brand-green); letter-spacing: 0.5px; text-transform: uppercase; line-height: 1; }
  .lockup__sub { font-size: 8px; font-weight: 700; color: var(--brand-blue); text-transform: uppercase; letter-spacing: 0.6px; margin-top: 4px; text-align: right; }
  .lockup__tagline { font-size: 8.5px; font-style: italic; font-weight: 700; color: var(--brand-blue); margin-top: 4px; letter-spacing: 0.3px; }
  .card--front .lockup { left: 18px; top: 36px; }
  .card--navy .lockup, .card--plain .lockup, .card--green .lockup { left: 50%; top: 30px; transform: translateX(-50%); }
  .card--navy .lockup__sub, .card--navy .lockup__tagline { color: #2c4aa6; }

  .swoosh { position: absolute; left: 0; top: 0; }

  .holder { position: absolute; left: 20px; top: 162px; }
  .holder__name { font-size: 24px; color: var(--ink); }
  .holder__role { font-size: 15px; color: var(--ink); margin-top: 4px; }

  .contact {
    position: absolute; right: 22px; top: 186px; text-align: right;
    font-size: 15px; line-height: 21px; color: #ffffff; font-style: normal;
  }

  .appointment { position: absolute; left: 118px; top: 172px; width: 360px; }
  .appointment__row { display: flex; align-items: flex-end; height: 32px; }
  .appointment__label { width: 48px; font-size: 15px; }
  .appointment__line { flex: 1; border-bottom: 1.5px solid var(--rule); margin-bottom: 3px; }
  .appointment__row--blank { padding-left: 48px; }
  .card--navy .appointment__line { border-color: #0c1540; }
</style>
</head>
<body>

  <section class="card card--front">
    <div class="lockup">
      <span class="lockup__dot"></span>
      <div class="lockup__text">
        <span class="lockup__name">Verdant Pathways</span>
        <span class="lockup__sub">Health and Fitness Center</span>
        <span class="lockup__tagline">Where Balanced Living is Your Truest Reward</span>
      </div>
    </div>

    <svg class="swoosh" width="560" height="323" viewBox="0 0 560 323" aria-hidden="true">
      <defs>
        <linearGradient id="wave-blue" x1="0" y1="0" x2="1" y2="0">
          <stop offset="0" stop-color="#e8edf7"/>
          <stop offset="0.3" stop-color="#7d92cc"/>
          <stop offset="0.7" stop-color="#2a4596"/>
          <stop offset="1" stop-color="#18306f"/>
        </linearGradient>
        <linearGradient id="wave-green" x1="0" y1="0" x2="1" y2="0">
          <stop offset="0" stop-color="#ffffff"/>
          <stop offset="0.3" stop-color="#6fbf63"/>
          <stop offset="1" stop-color="#2f8a2b"/>
        </linearGradient>
      </defs>
      <path d="M0 246 C170 238 360 170 560 84 L560 323 L0 323 Z" fill="url(#wave-green)"/>
      <path d="M0 262 C190 254 370 186 560 104 L560 323 L0 323 Z" fill="#ffffff"/>
      <path d="M0 268 C190 262 370 194 560 112 L560 323 L0 323 Z" fill="url(#wave-blue)"/>
    </svg>

    <div class="holder">
      <p class="holder__name">Marcus T. Delaney</p>
      <p class="holder__role">Owner/Health Practitioner</p>
    </div>

    <address class="contact">
      4172 Larchmont Ave S<br>
      Lakeford, MN 55788<br>
      Cell: 612-555-0147<br>
      Email: marcus.delaney@vpwellbody.com<br>
      www.vpwellbody.com
    </address>
  </section>

  <section class="card card--navy">
    <div class="lockup">
      <span class="lockup__dot"></span>
      <div class="lockup__text">
        <span class="lockup__name">Verdant Pathways</span>
        <span class="lockup__sub">Health and Fitness Center</span>
        <span class="lockup__tagline">Where Balanced Living is Your Truest Reward</span>
      </div>
    </div>
    <div class="appointment">
      <div class="appointment__row"><span class="appointment__label">Date:</span><span class="appointment__line"></span></div>
      <div class="appointment__row"><span class="appointment__label">Time:</span><span class="appointment__line"></span></div>
      <div class="appointment__row appointment__row--blank"><span class="appointment__line"></span></div>
    </div>
  </section>

  <section class="card card--plain">
    <div class="lockup">
      <span class="lockup__dot"></span>
      <div class="lockup__text">
        <span class="lockup__name">Verdant Pathways</span>
        <span class="lockup__sub">Health and Fitness Center</span>
        <span class="lockup__tagline">Where Balanced Living is Your Truest Reward</span>
      </div>
    </div>
    <div class="appointment">
      <div class="appointment__row"><span class="appointment__label">Date:</span><span class="appointment__line"></span></div>
      <div class="appointment__row"><span class="appointment__label">Time:</span><span class="appointment__line"></span></div>
      <div class="appointment__row appointment__row--blank"><span class="appointment__line"></span></div>
    </div>
  </section>

  <section class="card card--green">
    <div class="lockup">
      <span class="lockup__dot" style="background: var(--brand-blue)"></span>
      <div class="lockup__text">
        <span class="lockup__name" style="color: var(--brand-blue)">Verdant Pathways</span>
        <span class="lockup__sub">Health and Fitness Center</span>
        <span class="lockup__tagline">Where Balanced Living is Your Truest Reward</span>
      </div>
    </div>
    <div class="appointment">
      <div class="appointment__row"><span class="appointment__label">Date:</span><span class="appointment__line"></span></div>
      <div class="appointment__row"><span class="appointment__label">Time:</span><span class="appointment__line"></span></div>
      <div class="appointment__row appointment__row--blank"><span class="appointment__line"></span></div>
    </div>
  </section>

</body>
</html>
```